Educational handout for teachers (2 pages, A4)

We need a design for a tutorial for teachers in primary and secondary education that don't have (a lot of) experience with Computers. We made a powerpoint with the 'flow' of information and a few snippets of screenshots. Basically, it tells the story of what a teacher needs to do in preparation for the class ('LES VOORBEREIDING' in Dutch), and the second part is what the teacher (and student) need to do during class ('TIJDENS DE LES'). It's about learning a 'tool' (in this case Kwisvonk www.getkwisvonk.example) and use it in a class. Half way during the class, the activities split between teacher (what he shows on the big screen) and the students (what they can do on their own ipad/iphone). The main goal is that teachers are able to try out this new tool. The design should therefor be open, not frightening, visual appealing and still clear. Therefore we wrote down every step (1.a, b, c; 2.a ,b, c, etc) but if you have other ways to illustrate the flow of activities, that would be nice.
Requirements:
- 2 pager (A4, both sides) that can be printed and handed out to teachers
- first page (front) is a 'flow' of activities, which is easy to follow and supported with small snippets of screenshots. We made a few in example, but feel free to make new (better) ones. In the briefing powerpoint it is the "LES VOORBEREIDING" part, with the orange flow and the "TIJDENS DE LES" with the green flow. I used the colours just to make it clear for me. Please adjust the colours to fit your design, but stay 'close' to the logo of "Scholier 3040" attached.
- second page (back) of the A4 is a 3 column (or 3 rows) which explains the didactics. In the example below, we put the didactics in the same page (RESULTAAT (meaning results), TOEPASSINGEN (meaning applications), HOE VERDER (meaning next steps) but we want them moved to the back so there is more space in the front.
- We want it to be a 'template' so we can use it to fill it with other 'tools' (this one is only to explain how to use "Kwisvonk" in the classroom')
- It must use the design guides and therefore the "Scholier 3040" logo must be incorporated somewhere (can be small, but visible on the Front).
- We are on a tight deadline, so we want the final design by Thursday evening.
Any questions, feel free.
Updates
Industry/Entity Type
Education
Look and feel

```html
<!DOCTYPE html>
<html lang="nl">
<head>
<meta charset="utf-8">
<title>Tijdens de les – Kwisvonk</title>
<link href="https://fonts.googleapis.com/css2?family=Arimo:wght@400;700&family=Archivo+Black&family=Bebas+Neue&display=swap" rel="stylesheet">
<style>
:root{
  --blue:#0895d6;
  --title-blue:#1b63ad;
  --purple:#7c5fae;
  --magenta:#a93a90;
  --pink:#e6228c;
  --orange:#f28a33;
  --orange-badge:#d36d3c;
  --yellow:#fdc82f;
  --ink:#3a3a3a;
  --quiz-orange:#f7941d;
  --quiz-teal:#2ecfd0;
  --quiz-red:#e21b3c;
  --quiz-blue:#1368ce;
  --quiz-gold:#d89e00;
  --quiz-green:#26890c;
}
*{box-sizing:border-box;margin:0;padding:0}
html,body{width:928px;height:1200px;overflow:hidden;background:#fff}
body{font-family:"Arimo",Arial,sans-serif;color:var(--ink);position:relative}
.backdrop{position:absolute;inset:0}
.abs{position:absolute}
.page-title{left:570px;top:96px;font-family:"Bebas Neue",sans-serif;font-size:54px;letter-spacing:4px;color:var(--title-blue);line-height:1}
.badge{position:absolute;border-radius:50%;color:#fff;font-family:"Archivo Black",sans-serif;display:flex;align-items:center;justify-content:center;border:4px solid #fff;line-height:1}
.step-heading{font-family:"Archivo Black",sans-serif;font-weight:400;font-size:18px;color:#222;white-space:nowrap}
.step-list{font-size:15px;line-height:17.5px;list-style:none;white-space:nowrap}
.step-list u{text-decoration:underline}
.btn{position:absolute;display:flex;align-items:center;justify-content:center;color:#fff;font-size:11px;white-space:nowrap}
.btn-mine{left:249px;top:252px;width:100px;height:30px;background:#333;border-radius:2px}
.btn-play{left:359px;top:251px;width:76px;height:31px;background:#864cbf;font-family:"Archivo Black",sans-serif;font-size:16px;border-radius:2px}
.col-label{font-weight:700;font-size:14px}
.flow-text{font-size:12.5px;line-height:14px;white-space:nowrap}
.screen{position:absolute;border:1.5px solid #333;overflow:hidden;font-size:5.5px;line-height:6.5px}
.screen-bar{background:#fff;color:#222;text-align:center;padding:1px 10px;height:14px}
.brand{font-weight:700;color:#fff;font-size:12px}
.settings{left:604px;top:365px;width:138px;height:130px;background:var(--quiz-orange);border:2px solid #333}
.settings .row{display:flex;justify-content:space-between;color:#fff;padding:0 5px;height:12px;align-items:center;border-top:1px solid rgba(255,255,255,.4);font-size:4.5px}
.toggle{width:18px;height:6px;background:#fff;border-radius:1px;position:relative}
.toggle.on::after{content:"";position:absolute;left:0;top:0;width:8px;height:6px;background:#7ac943}
.toggle.off::after{content:"";position:absolute;right:0;top:0;width:8px;height:6px;background:#333}
.answers{display:grid;grid-template-columns:1fr 1fr;gap:1px}
.answers span{height:12px;color:#fff;padding-left:14px;display:flex;align-items:center}
</style>
</head>
<body>
<svg class="backdrop" width="928" height="1200" viewBox="0 0 928 1200">
  <path d="M0,0 H928 V45 C760,8 480,8 0,102 Z" fill="var(--blue)"/>
  <path d="M0,965 C260,1085 610,1170 928,1186 V1200 H0 Z" fill="var(--blue)"/>
  <circle cx="338" cy="195" r="140" fill="none" stroke="var(--purple)" stroke-width="7"/>
  <circle cx="670" cy="365" r="168" fill="none" stroke="var(--magenta)" stroke-width="12"/>
  <circle cx="318" cy="732" r="286" fill="none" stroke="var(--orange)" stroke-width="13"/>
  <circle cx="772" cy="990" r="146" fill="none" stroke="var(--yellow)" stroke-width="12"/>
</svg>

<h1 class="abs page-title">TIJDENSDELES</h1>

<!-- Stap 1 -->
<div class="badge" style="left:228px;top:76px;width:56px;height:56px;background:var(--purple);font-size:30px">1</div>
<h2 class="abs step-heading" style="left:264px;top:139px">Open de Quiz:</h2>
<ol class="abs step-list" style="left:230px;top:166px">
  <li>1. Ga naar <u>www.getkwisvonk.example</u></li>
  <li>2. Log in met jouw account</li>
  <li>3. Klik op MyKwisvonks (1)</li>
  <li>4. Klik op “Play”</li>
</ol>
<div class="btn btn-mine">&#9679; My Kwisvonks (1)</div>
<div class="btn btn-play">Play ▸</div>

<!-- Stap 2 -->
<div class="badge" style="left:547px;top:200px;width:60px;height:60px;background:var(--pink);font-size:32px">2</div>
<h2 class="abs step-heading" style="left:549px;top:276px">Voorbereiding van Quiz</h2>
<ol class="abs step-list" style="left:540px;top:306px;font-size:15.5px;line-height:18px">
  <li>1. Zet “Display Game PIN” op YES</li>
  <li>2. Zet ”Show minimized intro” op YES</li>
  <li>3. Toon op Digibord en klik op “Launch”</li>
</ol>
<div class="abs settings">
  <div class="brand" style="text-align:center;padding:4px 0">Kwisvonk</div>
  <div style="background:#fff;margin:0 3px;height:18px;font-size:6px;font-weight:700;display:flex;align-items:center;justify-content:center;color:#222">Nieuwe quiz voor in de les</div>
  <div style="margin:5px auto;width:26px;height:9px;background:#7ac943;color:#fff;font-size:4.5px;text-align:center;line-height:9px">Launch</div>
  <div class="row"><span>Display Game PIN throughout?</span><i class="toggle on"></i></div>
  <div class="row"><span>Show minimized intro instructions?</span><i class="toggle on"></i></div>
  <div class="row"><span>Randomize order of questions?</span><i class="toggle off"></i></div>
  <div class="row"><span>Randomize order of answers?</span><i class="toggle off"></i></div>
  <div class="row"><span>Play music while waiting?</span><i class="toggle off"></i></div>
</div>

<!-- Stap 3 -->
<div class="badge" style="left:292px;top:391px;width:92px;height:92px;background:var(--orange-badge);font-size:50px;border-width:5px">3</div>
<div class="abs col-label" style="left:193px;top:514px">Docent</div>
<div class="abs col-label" style="left:434px;top:512px">Leerling</div>

<p class="abs flow-text" style="left:154px;top:536px">1. Vertel de leerlingen<br>&nbsp;&nbsp;&nbsp;&nbsp;om in te loggen op<br>&nbsp;&nbsp;&nbsp;&nbsp;kwisvonk.example</p>
<p class="abs flow-text" style="left:405px;top:531px">2. Pakt telefoon, laptop<br>&nbsp;&nbsp;&nbsp;&nbsp;of tablet<br>3. Gaat naar <u>www.kwisvonk.example</u><br>4. Voert Pincode in<br>5. Voert naam in.</p>

<div class="screen" style="left:279px;top:512px;width:119px;height:90px;background:var(--quiz-teal)">
  <div class="screen-bar">Join at <b>kwisvonk.example</b> with Game PIN: <b>982659</b></div>
  <div style="display:flex;justify-content:space-between;padding:4px 4px;color:#fff"><b style="font-size:9px">0</b><span class="brand">Kwisvonk</span><span style="background:#9ee;padding:1px 3px">Start</span></div>
  <div style="position:absolute;bottom:0;left:0;right:0;height:17px;background:var(--quiz-blue);color:#fff;padding:5px 6px">&#9432; Waiting for players...</div>
</div>

<p class="abs flow-text" style="left:124px;top:638px">6.&nbsp; Wacht tot alle leerlingen<br>&nbsp;&nbsp;&nbsp;&nbsp;aangemeld zijn<br>7. Klik op “Start”</p>
<div class="screen" style="left:277px;top:619px;width:122px;height:82px;background:#f46f0a">
  <div class="screen-bar">Join at <b>kwisvonk.example</b> with Game PIN: <b>982659</b></div>
  <div style="display:flex;justify-content:space-between;padding:3px 5px;color:#fff"><b style="font-size:9px">21</b><span class="brand">Kwisvonk</span><span style="background:#333;padding:1px 3px">Start</span></div>
  <div style="color:#fff;padding:2px 6px;font-size:5.5px;line-height:9px">Ruben Sjors Mathilda Dries Charlie Sam Klaas Doris Greet Bas Bert Mila Harry Pim Egbert</div>
</div>

<p class="abs flow-text" style="left:87px;top:740px">8. Nu zie je de vraag met de<br>&nbsp;&nbsp;&nbsp;&nbsp;mogelijke antwoorden. De<br>&nbsp;&nbsp;&nbsp;&nbsp;leerlingen mogen nu stemmen!</p>
<p class="abs flow-text" style="left:413px;top:746px;font-size:12px">9. Nu begint de quiz! Kijk naar de<br>&nbsp;&nbsp;&nbsp;&nbsp;vraag en stem met je device!</p>
<div class="screen" style="left:279px;top:717px;width:119px;height:88px;background:#fff">
  <div class="screen-bar">Hoe heet de Griekse god van de zee</div>
  <div style="display:flex;align-items:center;justify-content:space-between;padding:2px 4px;height:44px">
    <span style="width:18px;height:18px;border-radius:50%;background:#864cbf;color:#fff;display:flex;align-items:center;justify-content:center;font-size:7px">13</span>
    <div role="img" aria-label="Beeld van een Griekse zeegod" style="width:44px;height:38px;background:linear-gradient(#8ecdf0,#c9a86a)"></div>
    <span style="text-align:center"><b>0</b><br>Answers</span>
  </div>
  <div class="answers">
    <span style="background:var(--quiz-red)">Hades</span><span style="background:var(--quiz-blue)">Zeus</span>
    <span style="background:var(--quiz-gold)">Poseidon</span><span style="background:var(--quiz-green)">Demeter</span>
  </div>
</div>

<p class="abs flow-text" style="left:122px;top:835px">9. Bekijk na afloop hoe de<br>&nbsp;&nbsp;&nbsp;&nbsp;antwoorden gegeven zijn.<br>&nbsp;&nbsp;&nbsp;&nbsp;Daarna krijg je ook de<br>&nbsp;&nbsp;&nbsp;&nbsp;score per leerling.</p>
<p class="abs flow-text" style="left:416px;top:835px">9. Bekijk na afloop hoe de<br>&nbsp;&nbsp;&nbsp;&nbsp;antwoorden gegeven zijn.<br>&nbsp;&nbsp;&nbsp;&nbsp;Daarna krijg je ook de<br>&nbsp;&nbsp;&nbsp;&nbsp;score per leerling.</p>
<div class="screen" style="left:279px;top:828px;width:119px;height:62px;background:#fff">
  <div class="screen-bar" style="height:10px">Hoe heet de Griekse god van de zee</div>
  <svg width="116" height="24" viewBox="0 0 116 24" style="display:block">
    <rect x="14" y="6" width="20" height="18" fill="var(--quiz-red)"/>
    <rect x="38" y="16" width="20" height="8" fill="var(--quiz-blue)"/>
    <rect x="62" y="3" width="20" height="21" fill="var(--quiz-gold)"/>
    <rect x="86" y="18" width="20" height="6" fill="var(--quiz-green)"/>
  </svg>
  <div class="answers" style="opacity:.55;margin-top:1px">
    <span style="background:var(--quiz-red)">Hades</span><span style="background:var(--quiz-blue)">Zeus</span>
    <span style="background:var(--quiz-gold)">Poseidon ✓</span><span style="background:var(--quiz-green)">Demeter</span>
  </div>
</div>

<svg class="abs" style="left:289px;top:908px" width="44" height="90" viewBox="0 0 44 90" role="img" aria-label="Telefoon met antwoordknoppen">
  <rect x="1" y="1" width="42" height="88" rx="6" fill="#111"/>
  <rect x="4" y="12" width="36" height="64" fill="#fff"/>
  <rect x="6" y="22" width="15" height="20" fill="var(--quiz-blue)"/>
  <rect x="23" y="22" width="15" height="20" fill="var(--quiz-red)"/>
  <rect x="6" y="44" width="15" height="20" fill="var(--quiz-green)"/>
  <rect x="23" y="44" width="15" height="20" fill="var(--quiz-gold)"/>
  <circle cx="22" cy="82" r="3" fill="#444"/>
</svg>
<p class="abs flow-text" style="left:338px;top:926px">10. De leerling ziet hoe ze<br>&nbsp;&nbsp;&nbsp;&nbsp;&nbsp;gescoord hebben en wie<br>&nbsp;&nbsp;&nbsp;&nbsp;&nbsp;de hoogste score heeft.</p>
</body>
</html>
```